Core Values Poster for Healthcare company

Trying to Create a core values poster for my company. Healthcare Company - We have Neurosurgery, Pain Management, Physical Therapy, Occupational Therapy, Rehab, Imaging, and psychology so far and we are growing fast.

Core Values would Include - (Execution), (Loyalty), (Innovation), (Synergy), (Growth-Oriented), (Ethics & Integrity), (Love), and (Energy)

Please incorporate the Company Logo which is on the website and I have included it in my uploads. As long as the logo stays blue it does not need a gradient effect.

I like the posters made for this contest : https://quillvane.com.au/poster-design/contests/make-team-principles-wallchart-815327

This picture should be memorable so people know our Core Values

Target Market(s)

Staff in the company

Colors

Designer to choose colors to be used in the design.

Requirements
Must have
• Logo
Nice to have
• Pictures for each core value

```html
<!DOCTYPE html>
<html lang="en">
<head>
<meta charset="utf-8">
<title>Core Values Poster</title>
<link rel="stylesheet" href="https://fonts.googleapis.com/css2?family=Montserrat:wght@800&family=Open+Sans:wght@800&display=swap">
<style>
  :root {
    --canvas: #939598;
    --frame: #ffffff;
    --green: #3db54a;
    --orange: #f7941d;
    --blue: #1071bb;
    --teal: #16a89e;
    --purple: #662d91;
    --slate: #939598;
    --pink: #d91c5c;
    --label: #ffffff;
    --icon: rgba(0, 0, 0, 0.22);
  }
  * { margin: 0; padding: 0; box-sizing: border-box; }
  html, body { width: 1200px; height: 848px; overflow: hidden; background: var(--canvas); }
  .poster { position: relative; width: 1200px; height: 848px; background: var(--canvas); }

  .brand-name {
    position: absolute; left: 24px; top: 18px;
    font-family: "Open Sans", sans-serif; font-weight: 800; font-size: 30px;
    color: var(--label); letter-spacing: 0.5px; line-height: 1;
  }
  .title {
    position: absolute; left: 306px; top: 8px;
    font-family: "Montserrat", sans-serif; font-weight: 800; font-size: 57px;
    color: #fff; letter-spacing: 1px; line-height: 1;
  }

  .frame { position: absolute; background: var(--frame); }
  .frame-top { left: 61px; top: 78px; width: 1079px; height: 300px; }
  .frame-bottom { left: 61px; top: 522px; width: 1079px; height: 300px; }
  .frame-center { left: 333px; top: 308px; width: 535px; height: 272px; }

  .value {
    position: absolute; display: flex; align-items: center; justify-content: center;
    overflow: hidden;
  }
  .value svg { position: absolute; inset: 0; width: 100%; height: 100%; }
  .value svg * { fill: none; stroke: var(--icon); stroke-width: 8; stroke-linejoin: round; stroke-linecap: round; }
  .value-label {
    position: relative; font-family: "Open Sans", sans-serif; font-weight: 800;
    color: var(--label); text-align: center; font-size: 47px; line-height: 1.13;
    letter-spacing: 0.5px;
  }
  .synergy { left: 73px; top: 90px; width: 343px; height: 276px; background: var(--green); }
  .ethics { left: 430px; top: 90px; width: 342px; height: 216px; background: var(--orange); overflow: visible; }
  .loyalty { left: 785px; top: 90px; width: 343px; height: 276px; background: var(--blue); }
  .innovation { left: 345px; top: 320px; width: 511px; height: 248px; background: var(--teal); }
  .execution { left: 73px; top: 534px; width: 343px; height: 276px; background: var(--purple); }
  .growth { left: 430px; top: 581px; width: 342px; height: 229px; background: var(--slate); }
  .love { left: 785px; top: 534px; width: 343px; height: 276px; background: var(--pink); }
  .synergy .value-label { margin-top: -2px; }
  .ethics .value-label { margin-top: 54px; }
  .loyalty .value-label { margin-top: -2px; }
  .execution .value-label { margin-top: 0; }
  .growth .value-label { margin-top: -44px; }
  .love .value-label { margin-top: -8px; }
</style>
</head>
<body>
<main class="poster">
  <div class="brand-name">CLEARVIEW</div>
  <h1 class="title">OUR CORE VALUES</h1>

  <div class="frame frame-top"></div>
  <div class="frame frame-bottom"></div>

  <section class="value synergy">
    <svg viewBox="0 0 343 276" aria-hidden="true">
      <circle cx="90" cy="48" r="28"/><path d="M40 150 Q40 95 90 92 Q140 95 140 150 Z"/>
      <circle cx="248" cy="48" r="28"/><path d="M198 150 Q198 95 248 92 Q298 95 298 150 Z"/>
      <circle cx="170" cy="115" r="32"/><path d="M93 268 Q93 170 170 165 Q247 170 247 268 Z"/>
    </svg>
    <div class="value-label">SYNERGY</div>
  </section>

  <section class="value ethics">
    <svg viewBox="0 0 342 216" aria-hidden="true">
      <path d="M120 210 V100 H150 L175 40 Q180 10 198 18 Q212 30 205 70 L198 100 H255 Q275 104 270 125 Q282 140 268 155 Q280 172 262 185 Q270 205 245 210 Z"/>
      <path d="M150 100 V210"/>
    </svg>
    <div class="value-label">ETHICS &amp;<br>INTEGRITY</div>
  </section>

  <section class="value loyalty">
    <svg viewBox="0 0 343 276" aria-hidden="true">
      <circle cx="171" cy="102" r="80"/>
      <path d="M145 80 L170 62 V140"/>
      <path d="M115 160 L85 240 L120 230 L140 255 L160 180"/>
      <path d="M227 160 L257 240 L222 230 L202 255 L182 180"/>
    </svg>
    <div class="value-label">LOYALTY</div>
  </section>

  <div class="frame frame-center"></div>
  <section class="value innovation">
    <svg viewBox="0 0 511 248" aria-hidden="true">
      <path d="M195 130 Q160 100 175 55 Q195 5 247 5 Q300 5 320 55 Q335 100 300 130 Q282 148 282 175 H212 Q212 148 195 130 Z"/>
      <path d="M214 195 H280 V215 Q280 240 247 240 Q214 240 214 215 Z"/>
      <path d="M262 68 L235 100 H262 L235 130"/>
      <path d="M140 82 H160 M335 82 H355 M160 20 L175 35 M335 20 L320 35 M160 150 L175 135 M335 150 L320 135"/>
    </svg>
    <div class="value-label">INNOVATION</div>
  </section>

  <section class="value execution">
    <svg viewBox="0 0 343 276" aria-hidden="true">
      <circle cx="155" cy="140" r="95" stroke-width="50" stroke-dasharray="26 24"/>
      <circle cx="155" cy="140" r="78" stroke-width="20"/>
      <path d="M140 110 L180 140 L140 170 Z"/>
    </svg>
    <div class="value-label">EXCECUTION</div>
  </section>

  <section class="value growth">
    <svg viewBox="0 0 342 229" aria-hidden="true">
      <path d="M100 225 H300"/>
      <path d="M105 145 H133 V225 H105 Z M155 115 H183 V225 H155 Z M205 80 H233 V225 H205 Z M255 50 H283 V225 H255 Z"/>
      <path d="M110 120 L180 75 L220 90 L290 10"/>
      <path d="M265 10 H290 V35"/>
    </svg>
    <div class="value-label">GROWTH-<br>ORIENTED</div>
  </section>

  <section class="value love">
    <svg viewBox="0 0 343 276" aria-hidden="true">
      <path d="M172 270 L55 150 Q15 100 45 60 Q85 15 140 40 Q160 52 172 70 Q184 52 204 40 Q259 15 299 60 Q329 100 289 150 Z" stroke-width="12"/>
    </svg>
    <div class="value-label">LOVE AND<br>ENERGY</div>
  </section>
</main>
</body>
</html>
```